VestoraHub.eu - need to polish our homepage (layout only)

We run a website project (http://cz.VestoraHub.eu) enabling free company formations via the Internet.

We now do complete redesign of the website which is almost ready but we still cannot get to proper shape of the homepage and we kindly ask you to participate on finalisation of this.

What we have now:
- design of sub-pages (see attached as NewSubPage design)

What must be preserved on homepage:
- upper horizontal menu and everything above it (logo, sign in button etc.)
- bottom quick navigation menu

What we would like to have (see attached HPSketch):
- unlike current homepage (http://cz.VestoraHub.eu) some introductory section just below the upper horizontal menu which will contain catching words/references

- more detailed website description and left navigation below this introductory section

- right banners stating amount of statutory fees and costs for registered office (if one chooses so)

- section for news

Thank you in advance for your proposals. In case of any queries please let us know.
Updates

Hello designers,

Many thanks for your first proposals, just.two general comments before I comment on particular designs:

1) We will probably want that the website does NOT include images of people but rather keep it as purely informative. The reason is that as we provide free service users often take us as sort of governmental agency and for such it is not very common here to have such type of public images on the website.

2) We will have 2 banners positions for our partners, one 970x200 leaderboard on the top of webpage and one left square below left navigation. You do not need to include them in your proposals, I am just mentioning this that this space must be left free for this purpose.

Many thanks for your effort so far, I will also comment separately on your particular designs.

Lukas

Requirements
Nice to have
• - you may consider substituting bullets in short catching sentences in introductory section by some icons expressing nature of the sentence

```html
<!DOCTYPE html>
<html lang="en">
<head>
<meta charset="utf-8">
<title>VestoraHub.eu – Free Company Formations Online</title>
<link href="https://fonts.googleapis.com/css2?family=Open+Sans:wght@400;600;700&display=swap" rel="stylesheet">
<style>
:root{
  --blue:#0d5aa7;
  --heading:#134d8c;
  --text:#555;
  --panel:#efefef;
  --border:#dcdcdc;
  --footer:#8c8c8c;
  --footer-dark:#737373;
  --orange:#f26b21;
  --violet:#8a3fd1;
  --dark-btn:#2d2d2d;
}
*{box-sizing:border-box;margin:0;padding:0}
html,body{width:747px;height:1200px;overflow:hidden}
body{position:relative;background:#fff;font-family:"Open Sans",Arial,sans-serif;color:var(--text)}
.abs{position:absolute}
.topline{left:0;top:0;width:747px;height:3px;background:#8f8f8f}

.brand{left:81px;top:31px;display:flex;align-items:center;gap:6px}
.brand-square{width:14px;height:14px;background:var(--blue)}
.brand-name{font-size:20px;font-weight:700;color:var(--blue);letter-spacing:-.3px}
.contact{left:362px;top:26px;font-size:9.5px;color:#333;line-height:15.5px}
.contact div{display:flex;align-items:center;gap:6px}
.signin{left:559px;top:31px;width:51px;height:22px;background:var(--blue);color:#fff;font-size:8.5px;font-weight:600;display:flex;align-items:center;justify-content:center;letter-spacing:.3px}
.newuser{left:622px;top:37px;font-size:8.5px;font-weight:600;color:#444;letter-spacing:.3px}

.mainnav{left:81px;top:74px;width:585px;height:34px;background:linear-gradient(#1466b8,#0a4d96);border:1px solid #083f7b}
.mainnav a{color:#fff;font-size:8.5px;font-weight:600;text-decoration:none;letter-spacing:.3px;position:absolute;top:12px}
.lang{right:8px;top:7px;width:70px;height:19px;background:#fff;border:1px solid #ccc;display:flex;align-items:center;padding-left:6px;gap:6px;font-size:7.5px;color:#333;font-weight:600}
.flag{width:13px;height:8px;background:#c8d4ea;border:1px solid #9aa}

.hero{left:81px;top:115px;width:585px;height:227px;border:1px solid #ccc;background:linear-gradient(90deg,#e9ecef 0%,#f4f4f4 55%,#efefef 100%)}
.hero-photo{left:0;top:0;width:263px;height:225px;background:linear-gradient(90deg,#8aa0b8 0%,#c9d2dc 40%,#e6e8ea 80%,rgba(240,240,240,0) 100%)}
.hero h1{left:276px;top:22px;font-size:18px;line-height:20px;font-weight:600;color:var(--heading);letter-spacing:.3px}
.hero ul{left:277px;top:68px;list-style:none;font-size:9.8px;color:#333}
.hero li{display:flex;align-items:center;gap:9px;height:20px}
.btn-dark{top:163px;height:24px;background:var(--dark-btn);color:#fff;font-size:8.5px;font-weight:600;display:flex;align-items:center;justify-content:center;letter-spacing:.3px;border:1px solid #111}

.counter{left:81px;top:352px;width:304px;height:73px;background:linear-gradient(#1466b8,#0a4d96);color:#fff;text-align:center;padding-top:8px}
.counter .lbl{font-size:15px;line-height:17px;letter-spacing:.4px}
.counter .num{font-size:18px;line-height:22px;letter-spacing:.3px}
.counter a{color:#fff;font-size:9px;text-decoration:underline;display:block;margin-top:2px}
.badge-box{top:352px;width:123px;height:73px;border:1px solid var(--border);background:#fff;display:flex;align-items:center;justify-content:center}

.subnav{left:81px;top:444px;width:585px;height:30px;background:linear-gradient(#b3b3b3,#8e8e8e);display:flex;align-items:center;justify-content:center;gap:13px;font-size:8.4px;font-weight:600;color:#fff;letter-spacing:.3px}

.welcome{left:81px;top:481px;width:387px;height:175px;border:1px solid var(--border);padding:14px 12px 0 12px}
.welcome h2{font-size:15px;font-weight:400;color:var(--heading);margin-bottom:7px}
.welcome p{font-size:8.3px;line-height:14.3px;color:#555;width:360px}
.learn{font-size:8px;font-weight:600;color:var(--blue);margin-top:10px;display:block}

.sidebox{left:479px;width:187px;background:var(--panel);padding:10px 12px}
.sidebox h3{font-size:9px;line-height:12px;font-weight:600;color:var(--heading);letter-spacing:.2px;margin-bottom:6px}
.price-row{display:flex;align-items:center;height:18px;border-bottom:1px solid #d6d6d6;font-size:7.5px;color:#555;gap:8px}
.tag{color:#fff;font-size:8.6px;font-weight:600;padding:0 6px;height:14px;line-height:14px}
.tag.violet{background:var(--violet);width:36px;text-align:center}
.tag.orange{background:var(--orange);width:46px;clip-path:polygon(0 0,88% 0,100% 50%,88% 100%,0 100%)}
.price-row b{font-size:10.5px;color:#333}
.price-row b.small{font-size:8.5px;font-weight:600}

.section-title{font-size:15px;color:var(--heading);font-weight:400}

.card{width:190px;height:106px;border:1px solid var(--border);padding:11px 8px 0 10px;display:flex;gap:5px;font-size:8px;line-height:12.4px;color:#555}
.card svg{flex:none;margin-top:2px}

.news{left:479px;top:704px;width:187px;height:339px;background:var(--panel);padding:12px 15px}
.news-item{border-bottom:1px solid #ccc;padding-bottom:9px;margin-bottom:10px;font-size:8px;line-height:12.4px}
.news-item .date{font-size:9.5px;color:#222;margin-bottom:1px}
.news-item .title{color:var(--blue);font-size:9px;font-weight:600;line-height:12.4px;margin-bottom:2px}
.news-item:last-of-type{border-bottom:none}
.more-btn{display:inline-block;background:var(--blue);color:#fff;font-size:8.5px;padding:5px 9px;margin-top:14px}

.footer{left:0;top:1062px;width:747px;height:106px;background:var(--footer)}
.fcol{top:1076px;color:#fff}
.fcol h4{font-size:9.5px;font-weight:600;margin-bottom:5px}
.fcol li{list-style:none;font-size:7.2px;line-height:15.5px;color:#eee;display:flex;align-items:center;gap:5px}
.ficon{width:9px;height:9px;background:#e3e3e3;display:inline-block}
.bottom{left:0;top:1168px;width:747px;height:32px;background:var(--footer-dark);color:#eee;font-size:7.4px}
</style>
</head>
<body>
<div class="abs topline"></div>

<header>
  <div class="abs brand"><span class="brand-square"></span><span class="brand-name">VestoraHub.eu</span></div>
  <div class="abs contact">
    <div><svg width="11" height="11" viewBox="0 0 11 11"><rect width="11" height="11" rx="2" fill="#0d5aa7"/><path d="M3 2.5c0 3 2 5.5 5 6l.8-1.4-1.5-.9-.7.7C5.6 6.5 4.6 5.5 4.3 4.4l.7-.7L4.1 2.2z" fill="#fff"/></svg>+420 - 221 555 018</div>
    <div><svg width="11" height="9" viewBox="0 0 11 9"><rect x=".5" y=".5" width="10" height="8" fill="none" stroke="#0d5aa7"/><path d="M.5.5l5 4 5-4" fill="none" stroke="#0d5aa7"/></svg>info@VestoraHub.eu</div>
  </div>
  <div class="abs signin">SIGN IN</div>
  <div class="abs newuser">NEW USER</div>
</header>

<nav class="abs mainnav">
  <svg class="abs" style="left:17px;top:10px" width="13" height="12" viewBox="0 0 13 12"><path d="M6.5 0L0 6h2v6h3.5V8h2v4H11V6h2z" fill="#fff"/></svg>
  <a style="left:56px">S.R.O. FORMATION</a>
  <a style="left:169px">TRADE LICENSE</a>
  <a style="left:268px">A.S. FORMATION</a>
  <div class="abs lang"><span class="flag"></span>ENG
    <svg class="abs" style="right:5px;top:7px" width="8" height="5" viewBox="0 0 8 5"><path d="M0 0h8L4 5z" fill="#999"/></svg></div>
</nav>

<section class="abs hero">
  <div class="abs hero-photo" role="img" aria-label="Hands typing on a keyboard in front of a computer monitor"></div>
  <h1 class="abs">FREE COMPANY FORMATIONS<br>ONLINE</h1>
  <ul class="abs">
    <li><svg width="10" height="9" viewBox="0 0 10 9"><path d="M1 5l3 3 5-7" fill="none" stroke="#0d5aa7" stroke-width="2"/></svg>Pay statutory registration fees only</li>
    <li><svg width="10" height="9" viewBox="0 0 10 9"><path d="M1 5l3 3 5-7" fill="none" stroke="#0d5aa7" stroke-width="2"/></svg>Simply without attending state authorities</li>
    <li><svg width="10" height="9" viewBox="0 0 10 9"><path d="M1 5l3 3 5-7" fill="none" stroke="#0d5aa7" stroke-width="2"/></svg>Registered capital from CZK 1</li>
    <li><svg width="10" height="9" viewBox="0 0 10 9"><path d="M1 5l3 3 5-7" fill="none" stroke="#0d5aa7" stroke-width="2"/></svg>Company formed in 3-5 days</li>
  </ul>
  <div class="abs btn-dark" style="left:277px;width:152px">TRY UNBINDING REGISTRATION</div>
  <div class="abs btn-dark" style="left:435px;width:97px">HOW IT WORKS</div>
</section>

<div class="abs counter">
  <div class="lbl">REGISTERED UP TO DATE</div>
  <div class="num">4345 firms</div>
  <a>Testimonials</a>
</div>
<div class="abs badge-box" style="left:402px"><svg width="60" height="60" viewBox="0 0 60 60" role="img" aria-label="Chamber of commerce membership badge"><circle cx="30" cy="30" r="28" fill="#f1f1f1" stroke="#c9c9c9"/><circle cx="30" cy="30" r="13" fill="#d9dde6"/></svg></div>
<div class="abs badge-box" style="left:544px"><svg width="60" height="60" viewBox="0 0 60 60" role="img" aria-label="Enterprise award badge"><rect x="8" y="8" width="44" height="44" fill="#e3edf6"/></svg></div>

<nav class="abs subnav">
  <span>HOW IT WORK</span><span>|</span><span>BEFORE BEGINNING</span><span>|</span><span>FORM COMPANY</span><span>|</span><span>CHECK REGISTRATION</span><span>|</span><span>FAQ</span><span>|</span><span>CONTACT</span>
</nav>

<section class="abs welcome">
  <h2>Welcome to Our Company WebSite</h2>
  <p>Aliquam molestie, mi et imperdiet euismod, dui purus auctor tellus, et interdum lacus lectus et ante. Sed accumsan sollicitudin sapien, sit amet adipiscing turpis gravida ac. In congue, neque ac lobortis volutpat, libero mauris varius mi, vitae suscipit ipsum ligula vitae risus. Duis aliquam nibh a dui iaculis viverra id a velit. Vivamus egestas risus in magna varius commodo. Sed semper viverra egestas. Etiam pretium porttitor lectus, vel ornare neque porta volutpat. Aenean a nibh eget turpis vehicula tempus ac sed massa. Vestibulum dolor nulla, ultrices ac tincidunt sed, laoreet non est.</p>
  <span class="learn">LEARN MORE</span>
</section>

<aside class="abs sidebox" style="top:481px;height:85px">
  <h3>STATUTORY COSTS ONLY,<br>NO COMMITMENTS!</h3>
  <div class="price-row"><span class="tag violet">S.R.O.</span>formation from CZK <b>12 000</b></div>
  <div class="price-row"><span class="tag violet">Ž.L.</span>&nbsp;&nbsp;formation from CZK <b>1 000</b></div>
</aside>
<aside class="abs sidebox" style="top:573px;height:83px">
  <h3>NEED ALSO A REGISTERED OFFICE?<br>DISCOUNT 25-100%</h3>
  <div class="price-row"><span class="tag orange">Prague</span>from CZK <b class="small">216/month</b></div>
  <div class="price-row"><span class="tag orange">Ostrava</span>from CZK <b class="small">436/month</b></div>
</aside>

<h2 class="abs section-title" style="left:81px;top:672px">Why VestoraHub.eu?</h2>
<h2 class="abs section-title" style="left:482px;top:672px">NEWS</h2>

<div class="abs card" style="left:81px;top:704px"><svg width="10" height="9" viewBox="0 0 10 9"><path d="M1 5l3 3 5-7" fill="none" stroke="#0d5aa7" stroke-width="1.8"/></svg><span>The only system in the Czech Republic enabling the complex formation of new companies online through the Internet, without complicated administration and running around state authorities.</span></div>
<div class="abs card" style="left:277px;top:704px"><svg width="10" height="9" viewBox="0 0 10 9"><path d="M1 5l3 3 5-7" fill="none" stroke="#0d5aa7" stroke-width="1.8"/></svg><span>Free of charge handling with the payment of statutory registration fees only. Save 60-80% of costs in comparison with the formation o companies through a law firm or the purchase of aready-made (shelf) company.</span></div>
<div class="abs card" style="left:81px;top:820px"><svg width="10" height="9" viewBox="0 0 10 9"><path d="M1 5l3 3 5-7" fill="none" stroke="#0d5aa7" stroke-width="1.8"/></svg><span>Short registration process, all documentation is generated automatically online and the registration is completed in short periods (usually 3-5 business days).</span></div>
<div class="abs card" style="left:277px;top:820px"><svg width="10" height="9" viewBox="0 0 10 9"><path d="M1 5l3 3 5-7" fill="none" stroke="#0d5aa7" stroke-width="1.8"/></svg><span>Simple and user-friendly online registration form enabling tailor-made company formation for each user.</span></div>
<div class="abs card" style="left:81px;top:938px"><svg width="10" height="9" viewBox="0 0 10 9"><path d="M1 5l3 3 5-7" fill="none" stroke="#0d5aa7" stroke-width="1.8"/></svg><span>Free-of-charge online formation of limited liability company (s.r.o.), trade license (ZL) and joint-stock company (a.s.). Possibility of another company forms through individual formation process.</span></div>
<div class="abs card" style="left:277px;top:938px"><svg width="10" height="9" viewBox="0 0 10 9"><path d="M1 5l3 3 5-7" fill="none" stroke="#0d5aa7" stroke-width="1.8"/></svg><span>Professional legal support during the whole course of the company registration and 100% guarantee of registration in the Company Register.</span></div>

<section class="abs news">
  <div class="news-item"><div class="date">30. 09. 2011</div><div class="title">Applies to The Startups of the Year Awards</div>Startups of the Year 2011 is a new competition, designated for starting entrepreneurs where va...</div>
  <div class="news-item"><div class="date">30. 09. 2011</div><div class="title">Applies to The Startups of the Year Awards</div>Startups of the Year 2011 is a new competition, designated for starting entrepreneurs where va...</div>
  <div class="news-item"><div class="date">30. 09. 2011</div><div class="title">Applies to The Startups of the Year Awards</div>Startups of the Year 2011 is a new competition, designated for starting entrepreneurs where va...</div>
  <span class="more-btn">Starsi Novinky</span>
</section>

<footer>
  <div class="abs footer"></div>
  <div class="abs fcol" style="left:81px"><h4>Vestora Hub</h4><ul><li>S.R.O.</li><li>Trade Lincense</li></ul></div>
  <div class="abs fcol" style="left:195px"><h4>Client Zone</h4><ul><li>My registration</li><li>Check Registration</li><li>My Profile</li></ul></div>
  <div class="abs fcol" style="left:311px"><h4>VestoraHub.eu</h4><ul><li>How it Works</li><li>Before Beginning</li><li>Business Conditions</li><li>Affiliate Programs</li></ul></div>
  <div class="abs fcol" style="left:444px"><h4>Support</h4><ul><li>FAQ</li><li>Contact</li></ul></div>
  <div class="abs fcol" style="left:537px"><h4>Connect us</h4><ul><li><span class="ficon"></span>Friendwall</li><li><span class="ficon"></span>Chirper</li><li><span class="ficon"></span>WorkLink</li><li><span class="ficon" style="background:#f39a3a"></span>Rss Feeds</li></ul></div>
  <div class="abs bottom"><span class="abs" style="left:81px;top:11px">Copyright © 2008 - 2013 NovaFirma.cz, all rights reserved</span><span class="abs" style="left:547px;top:11px">Developed by Larkfield Studio</span></div>
</footer>
</body>
</html>
```